Professional business cards for real estate development company

I need business cards for my new real estate development company. The company, "KORVA" is a real estate development, investment, and advisory firm with a focus on multifamily, office, and mixed-use projects across primary and secondary markets in the Southeast United States.

Style preference is modern

Industry/Entity Type

Real Estate Development

Contact Information for Business Card

The business cards need to include:
Name
Title
Mailing Address
Phone Number
Web Address

Logo is attached. I would like white to be the primary color with incorporation of the company colors: #232D3A and #B5A451

Font styles to use
Other font styles liked:
• Montserrat, Avenir

Requirements
Must have
• Company Logo. No need to include the company name since the name is in the logo.
Should not have
• No line type designs

```html
<!DOCTYPE html>
<html lang="en">
<head>
<meta charset="utf-8">
<title>KORVA Business Cards</title>
<link rel="stylesheet" href="https://fonts.googleapis.com/css2?family=Montserrat:wght@400;500;700&display=swap">
<style>
  :root {
    --navy: #232D3A;
    --gold: #B5A451;
    --paper: #F6F7F3;
    --backdrop: #E2E2E2;
    --navy-faint: #2C3746;
    --gold-faint: #BCAC5E;
    --muted: #4a5260;
  }
  * { margin: 0; padding: 0; box-sizing: border-box; }
  html, body { width: 1200px; height: 884px; overflow: hidden; }
  body {
    background: var(--backdrop);
    font-family: "Montserrat", sans-serif;
    color: var(--navy);
    position: relative;
  }
  .card {
    position: absolute;
    top: 280px;
    width: 540px;
    height: 324px;
    background: var(--paper);
    overflow: hidden;
    box-shadow: 0 2px 6px rgba(0,0,0,0.08);
  }
  .card--back { left: 40px; }
  .card--front { left: 620px; }
  .card__shapes { position: absolute; inset: 0; width: 100%; height: 100%; }

  .brand-name {
    position: absolute;
    font-weight: 700;
    color: var(--navy);
    letter-spacing: 0.04em;
    line-height: 1;
  }
  .card--back .brand-name { left: 36px; top: 34px; font-size: 17px; }
  .card--front .brand-name { left: 0; width: 460px; text-align: center; top: 122px; font-size: 58px; letter-spacing: 0.08em; }

  .headline {
    position: absolute;
    left: 156px;
    top: 76px;
    font-size: 21px;
    font-weight: 700;
    line-height: 1.32;
    text-transform: uppercase;
  }
  .tagline {
    position: absolute;
    left: 157px;
    top: 140px;
    font-size: 9px;
    letter-spacing: 0.06em;
    color: var(--muted);
  }
  .contact-list {
    position: absolute;
    left: 42px;
    top: 168px;
    list-style: none;
  }
  .contact-list li {
    display: flex;
    align-items: center;
    height: 24px;
    font-size: 14px;
    font-weight: 400;
    white-space: nowrap;
  }
  .contact-list li.contact--name { text-transform: uppercase; font-weight: 500; font-size: 15px; }
  .contact-list li.contact--title {
    height: 16px;
    margin-top: -4px;
    margin-bottom: 2px;
    padding-left: 21px;
    font-size: 9px;
    letter-spacing: 0.12em;
    text-transform: uppercase;
    color: var(--muted);
  }
  .contact-list svg { width: 12px; height: 12px; margin-right: 9px; fill: var(--gold); flex: none; }

  .web-line {
    position: absolute;
    left: 174px;
    top: 264px;
    display: flex;
    align-items: center;
    font-size: 15px;
  }
  .web-line svg { width: 13px; height: 13px; margin-right: 9px; fill: var(--navy); }

  .faint-mark {
    position: absolute;
    font-weight: 700;
    line-height: 1;
    letter-spacing: 0.06em;
  }
  .faint-mark--band {
    color: var(--navy-faint);
    font-size: 62px;
    left: 502px;
    top: 40px;
    transform-origin: left top;
    transform: rotate(90deg);
  }
  .faint-mark--corner {
    color: var(--gold-faint);
    font-size: 26px;
    left: 20px;
    top: 282px;
  }
</style>
</head>
<body>

  <section class="card card--back" aria-label="Card back with contact details">
    <svg class="card__shapes" viewBox="0 0 664 398" preserveAspectRatio="none" aria-hidden="true">
      <path fill="var(--gold)" d="M0 0 H330 C300 25 250 30 210 38 C160 48 150 90 120 120 C90 150 45 158 0 158 Z"/>
      <path fill="var(--navy)" d="M664 207 C600 215 560 280 520 312 C480 345 420 330 378 398 H664 Z"/>
    </svg>
    <div class="brand-name">KORVA</div>
    <h1 class="headline">Investment Advisory<br>Consulting</h1>
    <p class="tagline">real estate development company</p>
    <ul class="contact-list">
      <li class="contact--name">
        <svg viewBox="0 0 12 12"><circle cx="6" cy="3.2" r="2.8"/><path d="M0.5 12 C0.5 8 3 6.8 6 6.8 C9 6.8 11.5 8 11.5 12 Z"/></svg>Ellis Morane
      </li>
      <li class="contact--title">Managing Director</li>
      <li>
        <svg viewBox="0 0 12 12"><path d="M2.4 0.5 L4.6 3 L3.4 4.6 C4.2 6.3 5.7 7.8 7.4 8.6 L9 7.4 L11.5 9.6 L10 11.5 C5 11.2 0.8 7 0.5 2 Z"/></svg>555 - 0142 - 7781
      </li>
      <li>
        <svg viewBox="0 0 12 12"><path d="M0.5 2.5 H11.5 V9.5 H0.5 Z M1.2 3 L6 6.6 L10.8 3" stroke="var(--paper)" stroke-width="0.8"/></svg>hello@korvadev.com
      </li>
      <li>
        <svg viewBox="0 0 12 12"><path d="M6 0.5 C3.5 0.5 1.8 2.3 1.8 4.6 C1.8 7.6 6 11.5 6 11.5 C6 11.5 10.2 7.6 10.2 4.6 C10.2 2.3 8.5 0.5 6 0.5 Z"/><circle cx="6" cy="4.6" r="1.6" fill="var(--paper)"/></svg>120 Harbor Ave, Charlotte, NC 28202
      </li>
      <li>
        <svg viewBox="0 0 12 12"><circle cx="6" cy="6" r="5.5"/><path d="M0.5 6 H11.5 M6 0.5 V11.5 M1.5 3.3 H10.5 M1.5 8.7 H10.5" stroke="var(--paper)" stroke-width="0.7" fill="none"/></svg>www.korvadev.com
      </li>
    </ul>
  </section>

  <section class="card card--front" aria-label="Card front with company name">
    <svg class="card__shapes" viewBox="0 0 664 398" preserveAspectRatio="none" aria-hidden="true">
      <path fill="var(--gold)" d="M0 265 C60 255 120 265 170 300 C230 340 280 380 350 398 H0 Z"/>
      <path fill="var(--navy)" d="M572 0 H664 V398 H600 C540 390 500 360 500 300 C500 240 545 210 560 150 C575 90 565 40 572 0 Z"/>
    </svg>
    <div class="faint-mark faint-mark--band" aria-hidden="true">KORVA</div>
    <div class="faint-mark faint-mark--corner" aria-hidden="true">KORVA</div>
    <div class="brand-name">KORVA</div>
    <div class="web-line">
      <svg viewBox="0 0 12 12"><circle cx="6" cy="6" r="5.5"/><path d="M0.5 6 H11.5 M6 0.5 V11.5 M1.5 3.3 H10.5 M1.5 8.7 H10.5" stroke="var(--paper)" stroke-width="0.7" fill="none"/></svg>www.korvadev.com
    </div>
  </section>

</body>
</html>
```